"Harrow Crest Builders" is a residential building company and needs a new business card design and may re

We would like a redesign based on the existing logo, and would like to see a new font as well. We are bespoke home builders who build sustainable energy efficient homes.

Industry/Entity Type

Construction

Contact Information for Business Card

Business card size 40mm x 90mm

Colors

Designer to choose colors to be used in the design.

```html
<!DOCTYPE html>
<html lang="en">
<head>
<meta charset="utf-8">
<title>Harrow Crest Builders – Business Card</title>
<link rel="stylesheet" href="https://fonts.googleapis.com/css2?family=Open+Sans:wght@400;600;700&display=swap">
<style>
  :root {
    --page: #e6e4e1;
    --card: #151515;
    --card-edge: #1f1f1f;
    --accent: #9cbf2e;
    --ink: #f2f2f2;
    --muted: #8a8a8a;
    --rule: rgba(255,255,255,0.55);
  }
  * { box-sizing: border-box; margin: 0; padding: 0; }
  html, body {
    width: 1200px; height: 864px; overflow: hidden;
    background: var(--page);
    font-family: "Open Sans", Arial, sans-serif;
  }
  .sheet {
    width: 1200px; height: 864px;
    display: flex; flex-direction: column; align-items: center; justify-content: center;
    gap: 24px;
  }
  .card {
    width: 900px; height: 400px;
    background: linear-gradient(135deg, var(--card-edge), var(--card) 60%);
    border-radius: 4px;
    box-shadow: 0 10px 28px rgba(0,0,0,0.25);
    position: relative;
    color: var(--ink);
  }

  /* Front */
  .card-front {
    display: flex; flex-direction: column; align-items: center; justify-content: center;
    gap: 46px;
  }
  .brand { display: flex; align-items: center; gap: 18px; }
  .brand-square { width: 34px; height: 34px; background: var(--accent); flex: none; }
  .brand-name {
    font-weight: 600; color: var(--ink); letter-spacing: 0.5px; line-height: 1.05;
  }
  .card-front .brand-name { font-size: 52px; }
  .front-url {
    font-size: 17px; letter-spacing: 4px; color: var(--muted);
  }

  /* Back */
  .card-back {
    display: grid; grid-template-columns: 430px 2px 1fr; align-items: center;
    padding: 0 48px 0 56px;
  }
  .card-back .brand { gap: 14px; }
  .card-back .brand-square { width: 26px; height: 26px; }
  .card-back .brand-name { font-size: 34px; }
  .divider {
    width: 2px; height: 300px;
    background: linear-gradient(to bottom, transparent, var(--rule) 30%, var(--rule) 70%, transparent);
  }
  .details { padding-left: 36px; font-size: 18px; line-height: 1.42; }
  .person-name {
    color: var(--accent); font-weight: 700; font-size: 21px; letter-spacing: 0.5px;
    text-transform: uppercase; margin-bottom: 8px;
  }
  .company { font-weight: 700; }
  .contact-list { list-style: none; margin-top: 2px; }
  .contact-list li { display: flex; align-items: center; gap: 10px; }
  .contact-list svg { width: 15px; height: 15px; flex: none; }
  .contact-web { padding-left: 25px; }
</style>
</head>
<body>
<main class="sheet">

  <section class="card card-front" aria-label="Card front">
    <div class="brand">
      <span class="brand-square"></span>
      <span class="brand-name">Harrow Crest Builders</span>
    </div>
    <p class="front-url">www.harrowcrestbuilders.com.au</p>
  </section>

  <section class="card card-back" aria-label="Card back">
    <div class="brand">
      <span class="brand-square"></span>
      <span class="brand-name">Harrow Crest<br>Builders</span>
    </div>
    <span class="divider"></span>
    <div class="details">
      <p class="person-name">Daniel Rourke</p>
      <p class="company">Harrow Crest Builders Pty Ltd</p>
      <p>PO Box 4172 Eastgate</p>
      <p>LPO Hillview WA 6099</p>
      <p>Registration 40718</p>
      <p>ABN: 52 904 316 778</p>
      <ul class="contact-list">
        <li>
          <svg viewBox="0 0 16 16" aria-hidden="true"><rect x="4" y="1" width="8" height="14" rx="1.5" fill="var(--accent)"/><rect x="5.5" y="3" width="5" height="8" fill="var(--card)"/></svg>
          0400 555 019
        </li>
        <li>
          <svg viewBox="0 0 16 16" aria-hidden="true"><rect x="1" y="3" width="14" height="10" rx="1" fill="var(--accent)"/><path d="M1.5 3.5 L8 9 L14.5 3.5" fill="none" stroke="var(--card)" stroke-width="1.4"/></svg>
          daniel@harrowcrestbuilders.com.au
        </li>
        <li>
          <svg viewBox="0 0 16 16" aria-hidden="true"><circle cx="8" cy="8" r="7" fill="var(--accent)"/><path d="M1 8 H15 M8 1 C4 5 4 11 8 15 M8 1 C12 5 12 11 8 15" fill="none" stroke="var(--card)" stroke-width="1.1"/></svg>
          www.harrowcrestbuilders.com.au
        </li>
      </ul>
    </div>
  </section>

</main>
</body>
</html>
```